Corporate Design für Helfer bauen Brücken e.V. - Tiermedizin auf höchstem Niveau
Zielgruppe
(Bitte auch ergänzende Informationen im beigefügten Briefing-Dokumenten beachten!)
Helfer bauen Brücken ist der Förderverein der Veterinärklinik Haustiere der Adalbert-Konrad-Hochschule Passau. Der Verein ist gemeinnützig.
Als Förderverein der Veterinärklinik Haustiere der AKH ist es unser Ziel, die tiermedizinische Versorgung von Hunden und Katzen in Deutschland und international zum Wohl der Tiere stetig weiter zu verbessern. Im Rahmen unseres ideellen Geschäftsbetriebs als gemeinnützige Organisation ist es daher unsere Aufgabe, Mittel für die Verwirklichung dieses Ziels einzuwerben.
Um möglichst vielen Tieren eine optimale medizinische Versorgung zugänglich zu machen, setzen wir uns dafür ein, dass eine möglichst große Zahl von Tierärzten und Spezialisten auf höchstem Niveau ausgebildet werden kann.
Viele Krankheiten erfordern ein hohes Maß an tiefgreifendem Fachwissen, um Patienten nachhaltig helfen zu können. Daher gehört unsere besondere Aufmerksamkeit der Ausbildung von Spezialisten in den einzelnen medizinischen Disziplinen an der Veterinärklinik Haustiere. Gleichzeitig sehen wir es als unsere Aufgabe, die Öffentlichkeit zu informieren, wann es eines Spezialisten bedarf.
Spezialisten wissen innovative Behandlungsmethoden fachkundig anzuwenden. Durch wissenschaftlich fundierte Therapieentscheidungen verhelfen sie kranken Tieren wieder zu Lebensqualität und schenken ihnen damit neue Lebensfreude.
Weiterhin obliegt es uns, Wissenschaft und Forschung darin zu unterstützen, wertvolle Erkenntnisse für die Tiergesundheit zu gewinnen und dadurch Diagnostik und Therapie weiterzuentwickeln. Gleichzeitig fördern wir die Vermittlung und Verbreitung von wesentlichem Fachwissen.
Um bestmögliche Bedingungen für eine zukunftweisende Aus- und Fortbildung des tiermedizinischen Nachwuchses sowie für die Patientenbetreuung zu schaffen, fördern wir auch die Ausstattung der Mediz..
Aufgabenstellung
Die CD-Farben der Veterinärklinik Haustiere bzw. des Kliniklogos sind zwei Blautöne: RGB 16/66/124 und RGB 86/121/187.
Eine Anlehnung an das Kliniklogo bzw. die Farbgebung ist möglich, aber nicht zwingend erforderlich.
Eine weitere Farbe für eine akzentuierte Gestaltung ist erwünscht.
Aus der Bildmarke soll deutlich werden, dass Hunde und Katzen im Fokus stehen. Das Design soll einen professionellen, modernen und hochwertigen Eindruck vermitteln (Tiermedizin auf höchstem Niveau) und dynamisch wirken. Gleichzeitig soll es potentielle Spender und Förderer emotional berühren und inspirieren, sich für den Verein zu engagieren. Das Design kann sich an die Wort-Bild-Marke der Veterinärklinik Haustiere anlehnen, dies ist aber nicht zwingend erforderlich.

```html
<!DOCTYPE html>
<html lang="de">
<head>
<meta charset="utf-8">
<title>Helfer bauen Brücken e.V. – Geschäftsausstattung</title>
<link rel="stylesheet" href="https://fonts.googleapis.com/css2?family=Gabriela&family=Noto+Serif:wght@400;700&display=swap">
<style>
  :root {
    --stage: #353535;
    --paper: #ffffff;
    --paper-soft: #f3f3f3;
    --slate: #45647f;
    --sand: #c9b99b;
    --rule: #d6d6d6;
    --ink-light: #9a9a9a;
    --brand-font: "Gabriela", Georgia, serif;
    --body-font: "Noto Serif", Georgia, serif;
  }
  * { box-sizing: border-box; margin: 0; padding: 0; }
  html, body { width: 1200px; height: 1009px; overflow: hidden; }
  body { background: var(--stage); position: relative; font-family: var(--body-font); }

  .piece { position: absolute; background: var(--paper); overflow: hidden; }

  /* Wordmark */
  .wordmark { display: flex; align-items: center; gap: .35em; font-family: var(--brand-font); color: var(--slate); line-height: 1.05; }
  .wordmark .dot { flex: none; width: .9em; height: .9em; border-radius: 50%; background: var(--sand); }
  .wordmark .name { display: flex; flex-direction: column; }
  .wordmark .line-2 { padding-left: .6em; }

  .logo-panel { left: 46px; top: 35px; width: 468px; height: 204px; display: flex; align-items: center; justify-content: center; }
  .logo-panel .wordmark { font-size: 52px; }

  .phone-screen { left: 700px; top: 56px; width: 88px; height: 144px; background: var(--paper); }
  .phone-screen .wordmark { font-size: 10px; padding: 8px 6px 4px; }
  .phone-screen .photo { height: 54px; background: linear-gradient(90deg, #d9d4cc, #6d6b6a 45%, #e8e4de); }
  .phone-screen .band { position: absolute; left: 0; right: 0; bottom: 0; height: 32px; background: var(--slate); }

  .card-front { left: 879px; top: 126px; width: 188px; height: 115px; }
  .card-front .wordmark { font-size: 17px; padding: 22px 0 0 16px; }
  .card-front .band { position: absolute; left: 0; right: 0; top: 84px; height: 17px; background: var(--slate); }
  .card-front .band span { position: absolute; left: 20px; right: 20px; top: 5px; height: 7px; background: var(--paper); }

  .card-back { left: 879px; top: 291px; width: 188px; height: 115px; background: var(--sand); }
  .card-back .lines { position: absolute; left: 52px; top: 20px; display: flex; flex-direction: column; gap: 4px; }
  .card-back .lines span { display: block; height: 5px; background: var(--slate); }

  .envelope-back { left: 53px; top: 292px; width: 294px; height: 181px; background: var(--paper-soft); }
  .envelope-back svg { position: absolute; inset: 0; }

  .envelope-front { left: 404px; top: 335px; width: 293px; height: 136px; }
  .envelope-front .window { position: absolute; left: 24px; top: 61px; width: 123px; height: 52px; background: #e3e3e3; border: 1px solid var(--rule); border-radius: 3px; }
  .envelope-front .wordmark { position: absolute; left: 175px; top: 72px; font-size: 12px; }

  .folder { left: 116px; top: 515px; width: 587px; height: 379px; background: transparent; display: flex; gap: 0; }
  .folder .inner, .folder .cover { position: relative; width: 50%; height: 100%; background: var(--paper); }
  .folder .inner { background: var(--paper-soft); border-right: 1px solid var(--rule); }
  .folder .band { position: absolute; left: 0; right: 0; bottom: 18px; height: 13px; background: var(--slate); }
  .folder .cover .wordmark { position: absolute; left: 38px; top: 40px; font-size: 31px; }

  .letterhead { left: 805px; top: 521px; width: 288px; height: 369px; }
  .letterhead .wordmark { position: absolute; left: 88px; top: 14px; font-size: 15px; }
  .letterhead h2 { position: absolute; left: 0; right: 0; top: 84px; text-align: center; font: 700 6px/1 var(--body-font); color: var(--ink-light); }
  .letterhead p { position: absolute; left: 42px; right: 42px; top: 98px; font-size: 5px; line-height: 7.5px; color: var(--ink-light); text-align: justify; }
  .letterhead .band { position: absolute; left: 0; right: 0; bottom: 15px; height: 9px; background: var(--slate); }
</style>
</head>
<body>

  <section class="piece logo-panel" aria-label="Logo">
    <div class="wordmark"><span class="dot"></span><span class="name"><span>Helfer bauen</span><span class="line-2">Brücken e.V.</span></span></div>
  </section>

  <section class="piece phone-screen" aria-label="Mobile Startseite">
    <div class="wordmark"><span class="name"><span>Helfer bauen</span><span class="line-2">Brücken e.V.</span></span></div>
    <div class="photo" role="img" aria-label="Foto: Hunde und Katzen nebeneinander sitzend"></div>
    <div class="band"></div>
  </section>

  <section class="piece card-front" aria-label="Visitenkarte Vorderseite">
    <div class="wordmark"><span class="dot"></span><span class="name"><span>Helfer bauen</span><span class="line-2">Brücken e.V.</span></span></div>
    <div class="band"><span></span></div>
  </section>

  <section class="piece card-back" aria-label="Visitenkarte Rückseite">
    <div class="lines">
      <span style="width:84px"></span>
      <span style="width:84px"></span>
      <span style="width:84px"></span>
      <span style="width:84px"></span>
      <span style="width:68px"></span>
      <span style="width:60px"></span>
    </div>
    <div class="lines" style="top:96px"><span style="width:70px"></span></div>
  </section>

  <section class="piece envelope-back" aria-label="Briefumschlag Rückseite">
    <svg width="294" height="181" viewBox="0 0 294 181" aria-hidden="true">
      <path d="M0 0 H294 V22 Q290 46 270 46 H24 Q4 46 0 22 Z" fill="#e4e4e4"/>
      <path d="M0 46 H294" stroke="#d0d0d0" stroke-width="1"/>
    </svg>
  </section>

  <section class="piece envelope-front" aria-label="Briefumschlag Vorderseite">
    <div class="window"></div>
    <div class="wordmark"><span class="name"><span>Helfer bauen</span><span class="line-2">Brücken e.V.</span></span></div>
  </section>

  <section class="piece folder" aria-label="Präsentationsmappe">
    <div class="inner"><div class="band"></div></div>
    <div class="cover">
      <div class="wordmark"><span class="dot"></span><span class="name"><span>Helfer bauen</span><span class="line-2">Brücken e.V.</span></span></div>
      <div class="band"></div>
    </div>
  </section>

  <section class="piece letterhead" aria-label="Briefbogen">
    <div class="wordmark"><span class="name"><span>Helfer bauen</span><span class="line-2">Brücken e.V.</span></span></div>
    <h2>Lorem Ipsum</h2>
    <p>Sehr geehrte Damen und Herren, mit Ihrer Spende fördern Sie die Ausbildung von Spezialisten in der Tiermedizin. Jeder Beitrag hilft, Hunden und Katzen eine optimale Behandlung zu ermöglichen und neue Therapien zu erforschen. Wir danken Ihnen herzlich für Ihr Vertrauen und Ihre Unterstützung unserer Arbeit. Gemeinsam schaffen wir bessere Bedingungen für Patienten, Tierärzte und Forschung. Gerne informieren wir Sie über aktuelle Projekte, Veranstaltungen und Möglichkeiten, sich im Verein zu engagieren. Mit freundlichen Grüßen, Ihr Vorstand</p>
    <div class="band"></div>
  </section>

</body>
</html>
```